Landing Page for Martial Arts School

We'd like our page to look very much like http://www.tallpinestudio.com/. I've attached our text and you can see how I've tried to make it similar to their site in placement.
We'd like to do a darker green instead of their blue shading, obviously our logo (the dragon image) instead of theirs, our student photo or a better image you may choose, and instead of a solid block of text under "Welcome . . ." we'd like the USA Badge to the right of the text. At the bottom of the page we'd like a big button with our phone number. I know this is a lot to take in, but we're so looking forward to seeing your designs!

These designs are looking good! I'm sending each of you a few suggested tweaks for now! Best of luck!

As we enter the final few days of competition, I'd like to give a final word of thanks to all of our designers. We have moved out of good and into excellent, and we thank you all. We've also updated the student image we'd like you to use. All of the remaining designers will need to update their photos with the new one, please. Also, if you've one of the final designs, I'll be sending you a final set of notes and then we will be selecting someone. We may push back the final selection until Monday, depending.

Reason: We're going to discuss the finalized versions of your designs on Monday and make our final selection. If for some reason, none of the designers have made our suggested tweaks, then we still have another day.

```html
<!DOCTYPE html>
<html lang="en">
<head>
<meta charset="utf-8">
<title>Ridgeline TaeKwonDo</title>
<link rel="stylesheet" href="https://fonts.googleapis.com/css2?family=Open+Sans:wght@400;600;700&family=Arimo:wght@400;700&display=swap">
<style>
:root{
  --green:#3a7422;
  --green-dark:#2f6419;
  --green-text:#35781c;
  --black:#111;
  --ink:#333;
  --white:#fff;
  --grey:#8a8a8a;
  --badge:#d8262c;
}
*{box-sizing:border-box;margin:0;padding:0}
html,body{width:991px;height:1200px;overflow:hidden;background:var(--white)}
.page{position:relative;width:1200px;height:1453px;transform:scale(.82583);transform-origin:0 0;font-family:"Arimo",Arial,sans-serif;color:var(--ink)}
.abs{position:absolute}
.head-font{font-family:"Open Sans",Arial,sans-serif}

/* header */
.rule{left:0;top:118px;width:1200px;height:3px;background:var(--black)}
.nav-band{left:0;top:125px;width:1200px;height:44px;background:var(--green)}
.nav{left:513px;top:125px;height:44px;display:flex;list-style:none}
.nav li{height:44px;line-height:46px;color:var(--white);font-size:14px;letter-spacing:.3px}
.nav .active{background:var(--black);width:95px;text-align:center}
.nav .item{text-align:center}
.brand-mark{left:117px;top:10px;width:146px;height:146px;border-radius:50%;background:var(--white);border:5px solid var(--black)}
.brand-name{left:282px;top:52px;font-size:26px;font-weight:700;color:var(--green-text)}
.call-top{left:746px;top:34px;width:352px;height:67px;border-radius:4px;background:linear-gradient(#3a3a3a,#050505);display:flex;align-items:center;padding-left:12px;color:var(--white)}
.call-top .label{font-size:23px;margin-left:10px}
.call-top .num{font-size:28px;font-weight:700;margin-left:6px}

/* slider */
.slider{left:101px;top:193px;width:998px;height:323px;border:1px solid #ddd;overflow:hidden;display:flex}
.photo{height:100%}
.p1{width:306px;background:linear-gradient(180deg,#f3f3f3 0%,#e9e9e9 60%,#3d64c8 80%,#2a49a8 100%)}
.p2{width:386px;background:linear-gradient(180deg,#e9e4da 0%,#6b5a4a 45%,#1d1b1c 75%,#2a2626 100%)}
.p3{width:304px;background:linear-gradient(120deg,#c9b58a 0%,#a98e5f 40%,#2b2422 80%,#1a1616 100%)}
.arrow{top:333px;width:36px;height:32px;background:var(--black)}
.arrow-l{left:97px}.arrow-r{left:1066px}
.caption{left:315px;top:404px;width:545px;height:80px;background:rgba(0,0,0,.78);color:var(--white);text-align:center;padding-top:6px}
.caption .t1{font-size:26px;font-weight:700;line-height:34px}
.caption .t2{font-size:25px;line-height:36px}

/* welcome */
.welcome{left:102px;top:535px;font-size:30px;color:var(--green-text)}
.intro{left:104px;top:592px;width:735px;font-size:13px;line-height:22px}
.intro b{font-weight:700}
.badge{left:883px;top:591px;width:184px;height:186px}

/* classes */
.card{top:865px;width:301px;height:236px;border:1px solid #ddd;border-radius:5px;background:linear-gradient(#fff 30%,#e4e4e4)}
.card::after{content:"";position:absolute;left:20px;right:20px;bottom:-14px;height:10px;border-radius:50%;background:radial-gradient(ellipse at center,rgba(0,0,0,.28),rgba(0,0,0,0) 70%)}
.card-head{position:absolute;left:6px;top:6px;right:6px;height:35px;border-radius:4px;background:linear-gradient(var(--green),var(--green-dark));border:1px solid #6aa24b;color:var(--white);display:flex;justify-content:space-between;align-items:center;padding:0 6px 0 22px}
.card-head .title{font-size:23px}
.card-head .ages{font-size:18px;font-weight:700}
.card p{position:absolute;font-size:13px;line-height:22px;color:#333}

/* contact */
.contact-band{left:0;top:1175px;width:1200px;height:242px;background:var(--green)}
.contact-title{left:0;top:1214px;width:1200px;text-align:center;color:var(--white);font-size:30px}
.call-big{left:375px;top:1273px;width:472px;height:109px;border-radius:5px;background:linear-gradient(#2b2b2b,#141414);display:flex;align-items:center;padding-left:22px;color:var(--white)}
.call-big .label{font-size:30px;margin-left:24px}
.call-big .num{font-size:36px;font-weight:700;margin-left:8px}
.footer{left:0;top:1417px;width:1200px;height:36px;background:#050505;color:var(--grey);font-size:14px;text-align:center;line-height:38px}
</style>
</head>
<body>
<div class="page">

  <header>
    <div class="abs rule"></div>
    <div class="abs nav-band"></div>
    <ul class="abs nav">
      <li class="active">HOME</li>
      <li class="item" style="width:168px">ABOUT US</li>
      <li class="item" style="width:126px">CLASSES</li>
      <li class="item" style="width:206px">CONTACT US</li>
    </ul>
    <div class="abs brand-mark"></div>
    <div class="abs brand-name head-font">Ridgeline TKD</div>
    <div class="abs call-top head-font">
      <svg width="34" height="34" viewBox="0 0 24 24"><path fill="#fff" d="M6.6 10.8c1.4 2.8 3.8 5.1 6.6 6.6l2.2-2.2c.3-.3.7-.4 1-.2 1.1.4 2.3.6 3.6.6.6 0 1 .4 1 1V20c0 .6-.4 1-1 1C10.6 21 3 13.4 3 4c0-.6.4-1 1-1h3.5c.6 0 1 .4 1 1 0 1.3.2 2.5.6 3.6.1.3 0 .7-.2 1L6.6 10.8z"/></svg>
      <span class="label">Call Now :</span><span class="num">555.014.2378</span>
    </div>
  </header>

  <section class="abs slider">
    <div class="photo p1" role="img" aria-label="Instructor guiding a student through a board-breaking drill"></div>
    <div class="photo p2" role="img" aria-label="Row of young students in black uniforms and yellow belts"></div>
    <div class="photo p3" role="img" aria-label="Smiling young student in uniform in the training hall"></div>
  </section>
  <div class="abs arrow arrow-l"><svg width="36" height="32"><path d="M21 10l-6 6 6 6" stroke="#fff" stroke-width="2.5" fill="none"/></svg></div>
  <div class="abs arrow arrow-r"><svg width="36" height="32"><path d="M15 10l6 6-6 6" stroke="#fff" stroke-width="2.5" fill="none"/></svg></div>
  <div class="abs caption head-font">
    <div class="t1">Dedicated Masters &amp; Instructors</div>
    <div class="t2">teach students from age Three to Fourteen.</div>
  </div>

  <h1 class="abs welcome head-font" style="font-weight:400">Welcome to Ridgeline TaeKwonDo!</h1>
  <div class="abs intro">
    <p>Are you interested in Ridgeline TaeKwonDo classes, lessons, sparring, training, or one-on-one private tutoring in the martial arts? We are a full time martial arts academy based in Cedar Falls, TN. We offer a range of TaeKwonDo, or Korean Karate, classes for all skill levels, but we specialize in TaeKwonDo for kids and teens!</p>
    <p>TaeKwonDo training is in a safe, friendly school under the car of an instructor with 20 years of experience in martial arts. Our Instructor, Dan Holloway, was voted 2014’s Children’s Instructor of the Year by the National Martial Arts Guild! Learn with the best!</p>
    <p style="margin-top:22px"><b>We are located at 48 W. Main Street right in Downtown, Cedar Falls, TN.</b></p>
    <p>One block East of Harper’s Grill, across the street from Riverside Arts Center, Two Doors Down from Bluebird Jazz Room, and directly between Maple Bistro on Main and Still Water Yoga.</p>
  </div>
  <svg class="abs badge" viewBox="0 0 184 186" role="img" aria-label="Award badge">
    <circle cx="92" cy="93" r="88" fill="#fff" stroke="var(--badge)" stroke-width="6"/>
    <circle cx="92" cy="93" r="72" fill="none" stroke="#1d2f8a" stroke-width="2"/>
  </svg>

  <article class="abs card" style="left:102px">
    <div class="card-head head-font"><span class="title">Beginners</span><span class="ages">Ages 3-7</span></div>
    <p style="left:44px;top:70px;width:250px">It is a fun, energetic introduction to the art. Students begin to learn forms. This class accepts young students.</p>
  </article>
  <article class="abs card" style="left:452px">
    <div class="card-head head-font"><span class="title">Intermediate</span><span class="ages">Ages 6-15</span></div>
    <p style="left:18px;top:71px;width:262px">Children learn martial arts, respect, and self-defense in a safe environment. This class is based on experience level and accepts students with some experience in the art.</p>
  </article>
  <article class="abs card" style="left:795px">
    <div class="card-head head-font"><span class="title">Advanced</span><span class="ages">Ages 8-14</span></div>
    <p style="left:20px;top:68px;width:244px">For students who have some experience past the basic level. We cover more advanced topics, higher-kicks and more sparring. We prep our students for the challenges of confrontation, bullying, and self-defense.</p>
  </article>

  <section>
    <div class="abs contact-band"></div>
    <h2 class="abs contact-title head-font" style="font-weight:400">We’d Love to Hear From You!</h2>
    <div class="abs call-big head-font">
      <svg width="52" height="52" viewBox="0 0 52 52"><circle cx="26" cy="26" r="24" fill="none" stroke="#ccc" stroke-width="3"/><path transform="translate(12 12)" fill="#ddd" d="M6.6 10.8c1.4 2.8 3.8 5.1 6.6 6.6l2.2-2.2c.3-.3.7-.4 1-.2 1.1.4 2.3.6 3.6.6.6 0 1 .4 1 1V20c0 .6-.4 1-1 1C10.6 21 3 13.4 3 4c0-.6.4-1 1-1h3.5c.6 0 1 .4 1 1 0 1.3.2 2.5.6 3.6.1.3 0 .7-.2 1L6.6 10.8z"/></svg>
      <span class="label">Call Now :</span><span class="num">555.014.2378</span>
    </div>
  </section>

  <footer class="abs footer">Copyright © 2014 ridgelinetkd.com All Rights Reserved.</footer>
</div>
</body>
</html>
```